Business cards and logo for kitchen and bath remodeling company

We want an elegant card but that calls attention something unique and when people see it they remember us. A log that we can use for our own. We are a kitchen and bathroom remodeling company. We are 3 partners staring the company we are located in seattle washington usa. We try to give the best experience and luxury look in our projects and we are looking to show that in our cards. I added a sample of a card I really like. I like the black and gold look but gray blue or green in a metallic look would look nice. I'm open to any color.

Target Market(s)

Home owners.

Industry/Entity Type

Construction

Contact Information for Business Card

Larchmont and Vey builders

Colors

Designer to choose colors to be used in the design.

Requirements
Must have
• Make a Logo
• Logo to be unique
• Name of company larchmont and vey builders
Nice to have
• Have a good color scheme
• Front design to connect with back of card

```html
<!DOCTYPE html>
<html lang="en">
<head>
<meta charset="utf-8">
<title>Larchmont and Vey Builders – Business Card</title>
<link href="https://fonts.googleapis.com/css2?family=Poppins:wght@400;500;600&display=swap" rel="stylesheet">
<style>
  :root {
    --page: #1b1b1c;
    --card: #232324;
    --card-edge: #2e2e30;
    --gold: #d6a419;
    --rule: #8a9a2a;
    --ink: #f2f2f2;
  }
  * { box-sizing: border-box; margin: 0; padding: 0; }
  html, body {
    width: 1200px; height: 1200px; overflow: hidden;
    background: var(--page);
    font-family: "Poppins", sans-serif;
  }
  .sheet {
    width: 1200px; height: 1200px;
    display: flex; flex-direction: column; align-items: center; justify-content: center;
    gap: 90px;
  }
  .card {
    width: 640px; height: 366px;
    background: var(--card);
    border: 1px solid var(--card-edge);
    border-radius: 4px;
    box-shadow: 0 20px 40px rgba(0,0,0,.45);
    position: relative;
  }
  .brand {
    display: flex; align-items: center; gap: 14px;
  }
  .brand-square {
    width: 34px; height: 34px; background: var(--gold); flex: none;
  }
  .brand-name {
    color: var(--gold);
    font-weight: 500;
    text-transform: uppercase;
    letter-spacing: 1.5px;
    line-height: 1.15;
  }
  /* front */
  .card-front {
    display: flex; align-items: center; padding: 0 40px;
  }
  .card-front .brand { width: 270px; }
  .card-front .brand-name { font-size: 17px; }
  .divider {
    width: 1.5px; height: 210px; background: var(--rule); margin: 0 28px 0 20px;
  }
  .contact { color: var(--ink); font-size: 13px; }
  .contact-name { font-size: 20px; font-weight: 600; }
  .contact-title { color: var(--gold); font-size: 12px; margin-bottom: 14px; }
  .contact-line { display: flex; align-items: center; gap: 9px; margin-bottom: 6px; }
  .contact-line svg { width: 12px; height: 12px; fill: var(--gold); flex: none; }
  .contact-address { margin-top: 14px; line-height: 1.6; }
  /* back */
  .card-back {
    display: flex; align-items: center; justify-content: center;
  }
  .card-back .brand-square { width: 48px; height: 48px; }
  .card-back .brand-name { font-size: 26px; }
</style>
</head>
<body>
<main class="sheet">
  <section class="card card-front">
    <div class="brand">
      <span class="brand-square"></span>
      <span class="brand-name">Larchmont and Vey<br>builders</span>
    </div>
    <div class="divider"></div>
    <div class="contact">
      <p class="contact-name">Marcus Ellery</p>
      <p class="contact-title">Managing Director</p>
      <p class="contact-line">
        <svg viewBox="0 0 24 24"><path d="M6.6 10.8a15 15 0 0 0 6.6 6.6l2.2-2.2a1 1 0 0 1 1-.25 11.4 11.4 0 0 0 3.6.57 1 1 0 0 1 1 1V20a1 1 0 0 1-1 1A17 17 0 0 1 3 4a1 1 0 0 1 1-1h3.5a1 1 0 0 1 1 1c0 1.25.2 2.45.57 3.57a1 1 0 0 1-.25 1z"/></svg>
        206-555-0187
      </p>
      <p class="contact-line">
        <svg viewBox="0 0 24 24"><path d="M2 5h20v14H2z M2 5l10 8 10-8" /></svg>
        marcus@larchmontvey.com
      </p>
      <p class="contact-line">
        <svg viewBox="0 0 24 24"><circle cx="12" cy="12" r="10"/></svg>
        www.larchmontvey.com
      </p>
      <p class="contact-address">418 Alder Street NW<br>Suite 210, Seattle<br>WA 98104</p>
    </div>
  </section>

  <section class="card card-back">
    <div class="brand">
      <span class="brand-square"></span>
      <span class="brand-name">Larchmont and Vey<br>builders</span>
    </div>
  </section>
</main>
</body>
</html>
```